Comprehensive online math curriculum teaching service needs a PowerPoint design

We need a PowerPoint presentation for a startup company based in Edmonton, Alberta, Canada, called Vantoro Aritmética. Vantoro Aritmética is a comprehensive online math curriculum teaching service for independently schooled students in grades 6 through 12 worldwide. Teaching is done through a one-on-one, virtual adaptive classroom that uses integrated, interactive digital whiteboards for both teachers and students, with a standard modular lesson workflow for mastering math. Vantoro Aritmética is designed to help students from all socioeconomic backgrounds master mathematics. The creative brief also includes our logo.
Target Market(s)
Independently schooled students in grades 6 through 12 worldwide
Industry/Entity Type
Education - Mathematics Teaching
Look and feel

```html
<!DOCTYPE html>
<html lang="en">
<head>
<meta charset="utf-8">
<title>Vantoro Aritmética – Presentation Overview</title>
<link href="https://fonts.googleapis.com/css2?family=Poppins:ital,wght@0,400;0,500;0,600;0,700;1,400;1,600&family=Inter:wght@400;500;600&display=swap" rel="stylesheet">
<style>
:root{
  --page:#e4e4e4;
  --green:#24573f;
  --green-dark:#1b4330;
  --navy:#1e2b3b;
  --navy-board:#1f2a3a;
  --blue:#3b7be8;
  --blue-soft:#e9f0fd;
  --ink:#1c2430;
  --muted:#5b6473;
  --line:#c8ccd3;
  --ok:#2fb866;
  --no:#e23b3b;
  --help:#3b7be8;
  --row:#eeeff1;
}
*{box-sizing:border-box;margin:0;padding:0}
html,body{width:687px;height:1200px;overflow:hidden;background:var(--page)}
body{position:relative;font-family:"Inter",sans-serif;color:var(--ink)}
.slide{position:absolute;width:300px;height:168.5px;background:#fff;overflow:hidden;box-shadow:0 1px 2px rgba(0,0,0,.18)}
.abs{position:absolute}
.head{position:absolute;left:0;top:0;width:100%;height:26px;background:linear-gradient(90deg,var(--green-dark),var(--green) 60%,#2c6548)}
.head h2{position:absolute;left:15px;top:7px;font:600 9px/1 "Poppins",sans-serif;color:#fff;letter-spacing:.1px}
.brand-mini{position:absolute;right:15px;top:10px;display:flex;align-items:center;gap:2px;font:500 3.4px/1 "Poppins",sans-serif;color:#fff}
.brand-mini i{display:block;width:3.4px;height:3.4px;border-radius:50%;background:#fff}
.foot{position:absolute;left:15px;right:15px;bottom:9px;border-top:.5px solid var(--line)}
.foot span{position:absolute;left:0;top:3px;font:400 2.6px/1 "Inter",sans-serif;color:var(--muted);white-space:nowrap}
.foot b{position:absolute;right:0;top:3px;font:400 2.6px/1 "Inter",sans-serif;color:var(--muted)}
.ph{position:absolute}
.dot{position:absolute;border-radius:50%;background:var(--blue)}
.dot::after{content:"";position:absolute;inset:28%;border:.5px solid #fff;border-radius:1px}
/* cover slides */
.cover-board{position:absolute;inset:0;background:linear-gradient(135deg,#222d3d,#1a2433)}
.cover-band{position:absolute;left:0;top:58px;width:100%;height:52px;background:#fff}
.cover-name{display:flex;align-items:center;gap:5px;font:500 13px/1 "Poppins",sans-serif}
.cover-name i{display:block;width:10px;height:10px;border-radius:50%}
.cover-tag{font:400 5.6px/1 "Poppins",sans-serif}
/* slide 3 */
.intro{left:15px;top:39px;width:152px;font:italic 400 6.1px/8.6px "Poppins",sans-serif;color:var(--ink)}
.intro em{color:var(--blue);font-weight:600}
.founder{left:30px;top:117px;width:133px;height:21px;border-radius:0 10px 10px 0;background:linear-gradient(90deg,var(--blue-soft),rgba(233,240,253,0))}
.founder b{position:absolute;left:21px;top:4px;font:italic 700 6px/1 "Poppins",sans-serif;color:var(--blue)}
.founder span{position:absolute;left:21px;top:12px;font:italic 400 4.3px/1 "Poppins",sans-serif}
.photo-ring{left:13px;top:111px;width:33px;height:33px;border-radius:50%;border:1.2px solid var(--blue);background:#fff;display:flex;align-items:center;justify-content:center;font:400 4px/1 "Inter",sans-serif}
/* slide 4 */
.lbl{position:absolute;font:400 5px/5.8px "Inter",sans-serif;color:var(--ink)}
.lbl.r{text-align:right}
/* slide 5 */
.item{position:absolute;font:400 4.3px/5.1px "Inter",sans-serif}
/* slide 6 */
.panel{left:0;top:0;width:141px;height:100%;background:linear-gradient(160deg,#2c6548,var(--green-dark))}
.panel h2{position:absolute;left:15px;top:8px;width:120px;font:700 8.6px/9.4px "Poppins",sans-serif;color:#fff}
.panel p{position:absolute;left:15px;width:118px;font:italic 400 5.3px/6.6px "Poppins",sans-serif;color:#fff}
.panel .foot{right:0;border-color:rgba(255,255,255,.4)}
.panel .foot span{color:#dfe9e3}
.feat-t{left:152px;top:23px;font:italic 600 4.8px/1 "Poppins",sans-serif}
.feat{position:absolute;left:152px;width:130px;height:26px;border-radius:2px;background:linear-gradient(90deg,#e3ecfc,#f6f9fe);font:400 5.6px/6.4px "Poppins",sans-serif}
.feat .dot{left:6px;top:5px;width:15px;height:15px}
.feat span{position:absolute;left:26px;top:50%;transform:translateY(-50%)}
/* slide 7 */
.uc{position:absolute;width:132px;height:38px;border-radius:2px;background:linear-gradient(90deg,#e4ecfc,#f7f9fe)}
.uc .dot{left:5px;top:4px;width:10px;height:10px}
.uc b{position:absolute;left:5px;top:18px;width:40px;font:600 4.1px/4.6px "Poppins",sans-serif}
.uc i{position:absolute;left:45px;top:4px;bottom:4px;border-left:.5px solid #8e97a6}
.uc p{position:absolute;left:49px;top:5px;width:80px;font:400 3.1px/3.6px "Inter",sans-serif}
/* slide 8 */
.flow-h{position:absolute;left:15px;right:15px;height:0;border-top:.5px solid #8b93a0}
.flow-h span{position:absolute;left:50%;top:-3px;transform:translateX(-50%);background:#fff;padding:0 2px;font:600 4.8px/1 "Poppins",sans-serif;white-space:nowrap}
.fc{position:absolute;width:50px;border-radius:2px;background:linear-gradient(180deg,#e4ecfc,#f7f9fe)}
.fc .dot{left:3px;top:3px;width:8px;height:8px}
.fc b{position:absolute;left:14px;top:3.5px;width:35px;font:600 3.3px/3.7px "Poppins",sans-serif}
.fc p{position:absolute;left:14px;top:11px;width:35px;font:400 2.7px/3.1px "Inter",sans-serif;color:var(--muted)}
.arr{position:absolute;width:4.6px;height:4.6px;border-radius:50%;border:.4px solid #555;display:flex;align-items:center;justify-content:center;font:400 3px/1 "Inter",sans-serif}
/* slide 9 */
.who{position:absolute;top:33px;width:130px;height:119px;background:linear-gradient(180deg,#e9f0fd,#f6f8fd)}
.who h3{height:21px;display:flex;align-items:center;gap:5px;padding-left:7px;font:600 7.6px/1 "Poppins",sans-serif;color:#fff}
.who h3 i{display:block;width:12px;height:12px;border-radius:50%;background:#fff}
.who ul{list-style:none;padding:7px 8px 0 8px}
.who li{position:relative;padding-left:7px;margin-bottom:4.2px;font:400 5.5px/6.2px "Inter",sans-serif}
.who li::before{content:"→";position:absolute;left:0;top:0;color:var(--blue)}
/* slide 10 */
table.cmp{position:absolute;left:15px;top:31.5px;width:270px;border-collapse:collapse;table-layout:fixed}
.cmp th{height:14px;padding:0;background:var(--blue);color:#fff;font:500 4px/1 "Poppins",sans-serif;border-left:1.2px solid #fff}
.cmp th:first-child{text-align:left;padding-left:4px;border-left:0;width:82px;font-weight:600}
.cmp th.big{font:700 6px/1 "Poppins",sans-serif}
.cmp td{height:14.6px;padding:0;text-align:center;border-top:.6px solid #fff;font-size:0;line-height:0}
.cmp tr:nth-child(odd) td{background:#fff}
.cmp tr:nth-child(even) td{background:var(--row)}
.cmp td:first-child{text-align:left;padding-left:4px;font:600 3.2px/3.8px "Inter",sans-serif}
.mk{display:block;margin:0 auto;width:6px;height:6px}
.status{position:absolute;left:0;top:1077px;width:100%;text-align:center;font:400 17px/1 "Inter",sans-serif;letter-spacing:.3px;color:#111}
</style>
</head>
<body>
<svg width="0" height="0" style="position:absolute">
  <symbol id="ok" viewBox="0 0 10 10"><circle cx="5" cy="5" r="5" fill="#2fb866"/><path d="M2.8 5.2l1.5 1.5 3-3.2" stroke="#fff" stroke-width="1.1" fill="none"/></symbol>
  <symbol id="no" viewBox="0 0 10 10"><circle cx="5" cy="5" r="5" fill="#e23b3b"/><path d="M3.3 3.3l3.4 3.4M6.7 3.3l-3.4 3.4" stroke="#fff" stroke-width="1.1"/></symbol>
  <symbol id="q" viewBox="0 0 10 10"><circle cx="5" cy="5" r="5" fill="#3b7be8"/><text x="5" y="7.4" font-size="7" text-anchor="middle" fill="#fff" font-family="Inter,sans-serif">?</text></symbol>
</svg>

<!-- Slide 1: cover, dark board -->
<section class="slide" style="left:32.5px;top:33.5px">
  <div class="cover-board" role="img" aria-label="Dark chalkboard covered in handwritten math and physics formulas"></div>
  <div class="cover-band">
    <div class="abs cover-name" style="left:78px;top:13px;color:var(--navy)"><i style="background:var(--navy)"></i>Vantoro Aritmética</div>
    <div class="abs cover-tag" style="left:109px;top:36px;color:#444">Inspiring Math . Empowering Learning</div>
  </div>
</section>

<!-- Slide 2: cover, green board -->
<section class="slide" style="left:356.8px;top:33.5px">
  <div class="cover-board" style="background:linear-gradient(135deg,#2f6a4c,#1f4d37)" role="img" aria-label="Green chalkboard with faint handwritten algebra"></div>
  <div class="abs cover-name" style="left:78px;top:74px;color:#fff"><i style="background:#fff"></i>Vantoro Aritmética</div>
  <div class="abs cover-tag" style="left:109px;top:97px;color:#fff">Inspiring Math . Empowering Learning</div>
</section>

<!-- Slide 3: about -->
<section class="slide" style="left:32.5px;top:232.2px">
  <div class="head"><h2>Vantoro Aritmética</h2><div class="brand-mini"><i></i>Vantoro Aritmética</div></div>
  <p class="abs intro">A comprehensive online math curriculum teaching service for independently schooled students in grades <em>6 through 12 worldwide</em>. Teaching is done through our math academy, a one-on-one, virtual, adaptive classroom that uses integrated, interactive digital whiteboards for both teachers and students, with a standard, modular lesson workflow for mastering math.</p>
  <div class="abs founder"><b>Dr. Mateo Ravelli</b><span>Founder &amp; Lead Teacher</span></div>
  <div class="abs photo-ring">PHOTO</div>
  <div class="ph" style="left:178px;top:38px;width:122px;height:106px;border-radius:60px 0 0 60px;background:linear-gradient(135deg,#1f2b27,#3a4238 55%,#8a7a3a)" role="img" aria-label="Open book and pencils in front of a chalkboard with formulas"></div>
  <div class="foot"><span>Dr. Mateo Ravelli &nbsp;|&nbsp; Founder &amp; Lead Teacher &nbsp;|&nbsp; info@vantoroaritmetica.com</span><b>3</b></div>
</section>

<!-- Slide 4: problem wheel -->
<section class="slide" style="left:356.8px;top:232.2px">
  <div class="head"><h2>The Problem in Digital Math Education</h2><div class="brand-mini"><i></i>Vantoro Aritmética</div></div>
  <div class="lbl r" style="right:209px;top:44px">Current online tools<br>are not built for math</div>
  <div class="lbl r" style="right:209px;top:76px">Lack of comprehensive math<br>curricula based on<br>incremental and modular<br>lesson plans aimed at<br>mastery of math skills</div>
  <div class="lbl r" style="right:209px;top:129px">Students lose focus without<br>visual, hands-on interaction</div>
  <div class="lbl" style="left:209px;top:44px">Teachers struggle to explain<br>concepts without a whiteboard</div>
  <div class="lbl" style="left:209px;top:83px">Existing whiteboards lack<br>math-specific tools<br>and structure</div>
  <div class="lbl" style="left:209px;top:129px">Feedback is delayed,<br>and collaboration is limited</div>
  <svg class="abs" style="left:0;top:0" width="300" height="168.5" viewBox="0 0 300 168.5">
    <circle cx="150" cy="92" r="38.5" fill="none" stroke="#1e2b3b" stroke-width="23" stroke-dasharray="35.2 5.1" transform="rotate(-26 150 92)"/>
    <g fill="none" stroke="#fff" stroke-width=".7">
      <rect x="186" y="89" width="6" height="5"/><rect x="104" y="89" width="6" height="5" rx="2.5"/>
      <rect x="166" y="57" width="6" height="5"/><rect x="128" y="57" width="6" height="5"/>
      <rect x="166" y="122" width="6" height="5" rx="2.5"/><rect x="128" y="122" width="6" height="5" rx="2.5"/>
    </g>
  </svg>
  <div class="ph" style="left:129px;top:71px;width:42px;height:42px;border-radius:50%;background:radial-gradient(circle,#7d8b86,#3a5a4a)" role="img" aria-label="Stressed student at a laptop"></div>
  <div class="foot"><span>Dr. Mateo Ravelli &nbsp;|&nbsp; Founder &amp; Lead Teacher &nbsp;|&nbsp; info@vantoroaritmetica.com</span><b>4</b></div>
</section>

<!-- Slide 5: problem list -->
<section class="slide" style="left:32.5px;top:430.9px">
  <div class="head"><h2>The Problem in Digital Math Education</h2><div class="brand-mini"><i></i>Vantoro Aritmética</div></div>
  <div class="dot" style="left:15px;top:46px;width:14px;height:14px"></div>
  <div class="item" style="left:33px;top:48px">Current online tools<br>are not built for math</div>
  <div class="dot" style="left:99px;top:46px;width:14px;height:14px"></div>
  <div class="item" style="left:116px;top:45px">Teachers struggle<br>to explain concepts<br>without a whiteboard</div>
  <div class="dot" style="left:15px;top:85px;width:14px;height:14px"></div>
  <div class="item" style="left:33px;top:80px">Lack of comprehensive<br>math curricula based on<br>incremental and modular<br>lesson plans aimed at<br>mastery of math skills</div>
  <div class="dot" style="left:99px;top:85px;width:14px;height:14px"></div>
  <div class="item" style="left:116px;top:86px">Existing whiteboards<br>lack math-specific<br>tools and structure</div>
  <div class="dot" style="left:15px;top:123px;width:14px;height:14px"></div>
  <div class="item" style="left:33px;top:124px">Students lose focus<br>without visual,<br>hands-on interaction</div>
  <div class="dot" style="left:99px;top:123px;width:14px;height:14px"></div>
  <div class="item" style="left:116px;top:127px">Feedback is delayed,<br>and collaboration is limited</div>
  <div class="ph" style="left:178px;top:38px;width:122px;height:106px;border-radius:60px 0 0 60px;background:linear-gradient(135deg,#2f5a46,#5b6a60 55%,#c9c2b8)" role="img" aria-label="Frustrated student holding a sheet in front of a green chalkboard"></div>
  <div class="foot"><span>Dr. Mateo Ravelli &nbsp;|&nbsp; Founder &amp; Lead Teacher &nbsp;|&nbsp; info@vantoroaritmetica.com</span><b>5</b></div>
</section>

<!-- Slide 6: solution -->
<section class="slide" style="left:356.8px;top:430.9px">
  <div class="abs panel">
    <h2>Vantoro Aritmética:<br>A Purpose-Built Comprehensive Math Curriculum Virtual Teaching Service Central line</h2>
    <p style="top:85px">Vantoro Aritmética brings teachers and students together in an interactive, real-time virtual math classroom.</p>
    <p style="top:109px">Vantoro Aritmética delivers a pedagogical approach for rapid mastery of mathematical concepts and skills.</p>
    <div class="foot"><span>Dr. Mateo Ravelli &nbsp;|&nbsp; Founder &amp; Lead Teacher &nbsp;|&nbsp; info@vantoroaritmetica.com</span></div>
  </div>
  <div class="brand-mini" style="color:var(--ink)"><i style="background:var(--ink)"></i>Vantoro Aritmética</div>
  <div class="abs feat-t">Features to highlight:</div>
  <div class="feat" style="top:32px"><div class="dot"></div><span>Collaborative digital whiteboards</span></div>
  <div class="feat" style="top:62px"><div class="dot"></div><span>Math-specific tools<br>(geometry, equations, graphs)</span></div>
  <div class="feat" style="top:91px"><div class="dot"></div><span>Teacher-student workspaces<br>and live feedback</span></div>
  <div class="feat" style="top:121px"><div class="dot"></div><span>Comprehensive curricula<br>designed for rapid mastery of math</span></div>
  <div class="foot" style="left:141px;border:0"><b>6</b></div>
</section>

<!-- Slide 7: unique -->
<section class="slide" style="left:32.5px;top:629.6px">
  <div class="head"><h2>What Makes Vantoro Aritmética Unique?</h2><div class="brand-mini"><i></i>Vantoro Aritmética</div></div>
  <div class="uc" style="left:15px;top:33.5px"><div class="dot"></div><b>Innovative Lesson Design</b><i></i><p>Our lessons are designed for 1½-hour sessions, each covering a new math concept that can be taught in 20 minutes, allowing students ample time to practice the newly introduced math skills daily.</p></div>
  <div class="uc" style="left:152px;top:33.5px"><div class="dot"></div><b>Engagement and Mastery</b><i></i><p>Our lessons are designed for 1½-hour sessions, each covering a new math concept that can be taught in 20 minutes, allowing students ample time to practice the newly introduced math skills daily.</p></div>
  <div class="uc" style="left:15px;top:75px"><div class="dot"></div><b>Comprehensive Math Teaching</b><i></i><p style="top:10px">Comprehensive online math curriculum teaching service for independently schooled students in grades 6 through 12 worldwide.</p></div>
  <div class="uc" style="left:152px;top:75px"><div class="dot"></div><b>Frequent Assessments</b><i></i><p style="top:10px">Comprehensive online math curriculum teaching service for independently schooled students in grades 6 through 12 worldwide.</p></div>
  <div class="uc" style="left:15px;top:116px"><div class="dot"></div><b>Effective Curricula</b><i></i><p style="top:4px">Time-tested and proven pedagogical methodology with three pillars: (1) new math concepts built on previously taught ones; (2) daily review of earlier math concepts to increase understanding; and (3) frequent, cumulative assessments to ensure students master each math skill as new ones are added.</p></div>
  <div class="uc" style="left:152px;top:116px"><div class="dot"></div><b>Synchronous Class Sessions</b><i></i><p style="top:4px">Time-tested and proven pedagogical methodology with three pillars: (1) new math concepts built on previously taught ones; (2) daily review of earlier math concepts to increase understanding; and (3) frequent, cumulative assessments to ensure students master each math skill as new ones are added.</p></div>
  <div class="foot"><span>Dr. Mateo Ravelli &nbsp;|&nbsp; Founder &amp; Lead Teacher &nbsp;|&nbsp; info@vantoroaritmetica.com</span><b>7</b></div>
</section>

<!-- Slide 8: how it works -->
<section class="slide" style="left:356.8px;top:629.6px">
  <div class="head"><h2>How Vantoro Aritmética Works</h2><div class="brand-mini"><i></i>Vantoro Aritmética</div></div>
  <div class="flow-h" style="top:33px"><span>FLOW (TEACHER'S VIEW)</span></div>
  <div class="fc" style="left:15px;top:38px;height:25px"><div class="dot"></div><b>Innovative Lesson Design</b><p style="top:10px">Name it, select grade/topic</p></div>
  <div class="fc" style="left:70px;top:38px;height:25px"><div class="dot"></div><b>Invite Students</b><p style="top:10px">Share a class code or link</p></div>
  <div class="fc" style="left:125px;top:38px;height:25px"><div class="dot"></div><b>Launch Session</b><p style="top:10px">Start a live whiteboard and teach a lesson</p></div>
  <div class="fc" style="left:179px;top:38px;height:25px"><div class="dot"></div><b>Interact in Real Time</b><p style="top:10px">Students write/ draw alongside the teacher</p></div>
  <div class="fc" style="left:234px;top:38px;height:25px"><div class="dot"></div><b>Review Work</b><p style="top:10px">Teachers give comments or assign practice</p></div>
  <div class="flow-h" style="top:74.5px"><span>FLOW (STUDENT'S VIEW)</span></div>
  <div class="fc" style="left:15px;top:80px;height:33px"><div class="dot"></div><b>Receive Class Link</b><p style="top:10px">Click the link and enter the class code</p></div>
  <div class="fc" style="left:70px;top:80px;height:33px"><div class="dot"></div><b>Attend Class</b><p style="top:10px">Join class session</p></div>
  <div class="fc" style="left:125px;top:80px;height:33px"><div class="dot"></div><b>Participate in Class</b><p style="top:10px">Listen to the lecture, take notes, ask questions</p></div>
  <div class="fc" style="left:179px;top:80px;height:33px"><div class="dot"></div><b>Solve Practice Problems</b><p style="top:10px">Solve facts practice, lesson practice and other in-class practice problems and homework on their whiteboard</p></div>
  <div class="fc" style="left:234px;top:80px;height:33px"><div class="dot"></div><b>Take Test</b><p style="top:7px">Take in-class tests</p></div>
  <div class="flow-h" style="top:119px"><span>FLOW (PARENT/GUARDIAN'S VIEW)</span></div>
  <div class="fc" style="left:15px;top:124.5px;height:29px"><div class="dot"></div><b>Register Student</b><p style="top:10px">Register student</p></div>
  <div class="fc" style="left:70px;top:124.5px;height:29px"><div class="dot"></div><b>Pay Tuition</b><p style="top:7px">Pay tuition fee</p></div>
  <div class="fc" style="left:125px;top:124.5px;height:29px"><div class="dot"></div><b>Attend Free Consultation</b><p style="top:10px">Register and attend free consultation</p></div>
  <div class="fc" style="left:179px;top:124.5px;height:29px"><div class="dot"></div><b>Progress Tracking</b><p style="top:10px">Receive detailed analytics and regular progress reports on one's own child's performance.</p></div>
  <div class="fc" style="left:234px;top:124.5px;height:29px"><div class="dot"></div><b>Active Involvement</b><p style="top:10px">Actively involved in student math education, use weekly office hours to ask questions</p></div>
  <div class="arr" style="left:66px;top:51px">›</div><div class="arr" style="left:121px;top:51px">›</div><div class="arr" style="left:175px;top:51px">›</div><div class="arr" style="left:229.5px;top:51px">›</div>
  <div class="arr" style="left:66px;top:95px">›</div><div class="arr" style="left:121px;top:95px">›</div><div class="arr" style="left:175px;top:95px">›</div><div class="arr" style="left:229.5px;top:95px">›</div>
  <div class="arr" style="left:66px;top:139px">›</div><div class="arr" style="left:121px;top:139px">›</div><div class="arr" style="left:175px;top:139px">›</div><div class="arr" style="left:229.5px;top:139px">›</div>
  <div class="foot"><span>Dr. Mateo Ravelli &nbsp;|&nbsp; Founder &amp; Lead Teacher &nbsp;|&nbsp; info@vantoroaritmetica.com</span><b>8</b></div>
</section>

<!-- Slide 9: audience -->
<section class="slide" style="left:32.5px;top:828.3px">
  <div class="head"><h2>Who Is Vantoro For?</h2><div class="brand-mini"><i></i>Vantoro Aritmética</div></div>
  <div class="who" style="left:15px">
    <h3 style="background:var(--blue)"><i></i>Target Users</h3>
    <ul>
      <li>English-speaking grades 6–12 independently schooled students worldwide</li>
      <li>Working parents of grades 6–12 independently schooled students</li>
      <li>Internationally travelling parents with grades 6–12 independently schooled students</li>
      <li>Remote schools that are struggling to find qualified grade 6-12 math teachers</li>
    </ul>
  </div>
  <div class="who" style="left:154px">
    <h3 style="background:var(--navy)"><i></i>Opportunity</h3>
    <ul>
      <li>Over 4 million independently schooled students in English-speaking countries: USA 3+ million; Canada 100,000; UK 57,000; and Australia 30,000</li>
      <li>Shortage of qualified mathematics teachers and tutors</li>
      <li>Latin America + U.S + Canada have a high demand for bilingual math education</li>
      <li>Math is consistently the most challenging subject in middle and high schools</li>
    </ul>
  </div>
  <div class="foot"><span>Dr. Mateo Ravelli &nbsp;|&nbsp; Founder &amp; Lead Teacher &nbsp;|&nbsp; info@vantoroaritmetica.com</span><b>9</b></div>
</section>

<!-- Slide 10: comparison -->
<section class="slide" style="left:356.8px;top:828.3px">
  <div class="head"><h2>How Vantoro Aritmética Stands Out</h2><div class="brand-mini"><i></i>Vantoro Aritmética</div></div>
  <table class="cmp">
    <thead><tr><th>Feature / App</th><th class="big">Quizlo</th><th class="big" style="font-weight:400">Plotra</th><th>SlateHub</th><th>Orbit Academy</th><th>Vantoro Aritmética</th></tr></thead>
    <tbody>
      <tr><td>Math-focused design</td><td><svg class="mk"><use href="#ok"/></svg></td><td><svg class="mk"><use href="#no"/></svg></td><td><svg class="mk"><use href="#no"/></svg></td><td><svg class="mk"><use href="#ok"/></svg></td><td><svg class="mk"><use href="#ok"/></svg></td></tr>
      <tr><td>Real-time collaboration</td><td><svg class="mk"><use href="#ok"/></svg></td><td><svg class="mk"><use href="#no"/></svg></td><td><svg class="mk"><use href="#ok"/></svg></td><td><svg class="mk"><use href="#no"/></svg></td><td><svg class="mk"><use href="#ok"/></svg></td></tr>
      <tr><td>Geometry/graphing tools</td><td><svg class="mk"><use href="#ok"/></svg></td><td><svg class="mk"><use href="#ok"/></svg></td><td><svg class="mk"><use href="#no"/></svg></td><td><svg class="mk"><use href="#ok"/></svg></td><td><svg class="mk"><use href="#ok"/></svg></td></tr>
      <tr><td>Integrated student-teacher whiteboards</td><td><svg class="mk"><use href="#no"/></svg></td><td><svg class="mk"><use href="#no"/></svg></td><td><svg class="mk"><use href="#ok"/></svg></td><td><svg class="mk"><use href="#no"/></svg></td><td><svg class="mk"><use href="#ok"/></svg></td></tr>
      <tr><td>Feedback system</td><td><svg class="mk"><use href="#ok"/></svg></td><td><svg class="mk"><use href="#no"/></svg></td><td><svg class="mk"><use href="#ok"/></svg></td><td><svg class="mk"><use href="#ok"/></svg></td><td><svg class="mk"><use href="#ok"/></svg></td></tr>
      <tr><td>Modular standard math lessons</td><td><svg class="mk"><use href="#q"/></svg></td><td><svg class="mk"><use href="#no"/></svg></td><td><svg class="mk"><use href="#no"/></svg></td><td><svg class="mk"><use href="#no"/></svg></td><td><svg class="mk"><use href="#ok"/></svg></td></tr>
      <tr><td>Comprehensive grade math curricula, including frequent assessments</td><td><svg class="mk"><use href="#no"/></svg></td><td><svg class="mk"><use href="#no"/></svg></td><td><svg class="mk"><use href="#no"/></svg></td><td><svg class="mk"><use href="#no"/></svg></td><td><svg class="mk"><use href="#ok"/></svg></td></tr>
    </tbody>
  </table>
  <div class="foot"><span>Dr. Mateo Ravelli &nbsp;|&nbsp; Founder &amp; Lead Teacher &nbsp;|&nbsp; info@vantoroaritmetica.com</span><b>10</b></div>
</section>

<p class="status">DESIGN STILL ON PROGRESS</p>
</body>
</html>
```